Business Card Design for new consultancy company

Name of Company: Orbit Lanternway
Nature of Business: Digital Business Consultancy
Specialises in Digital Media Strategy, Digital Business Model Transformation, Over-The-Top (OTT) Development, Web Business Development, Digital Marketing, Web and App Product Development, Design and Innovation

Website: http://www.orbit-lanternway.example

Designs can be of any colour or any number of colours, objective is to give the impression we are a digital trend setter, creative and impactful.

Also please suggest a logo to complement the name and business card.

Target Market(s)

Media Companies, Telcos, Enterprises

Industry/Entity Type

Business

Contact Information for Business Card

Standard business card size. OK with to play with small variations like corners for impact/impression.

Font styles to use
Serif
Sans Serif

Requirements
Must have
• Clarity, Impact, Creativity
Nice to have
• Design should encapsulate professionalism, expertise, yet trend-setting and vibrant for digital consultancy
Should not have
• Messy layout, too gaudy colours or design

```html
<!DOCTYPE html>
<html lang="en">
<head>
<meta charset="utf-8">
<title>Orbit Lanternway – Business Card</title>
<link rel="stylesheet" href="https://fonts.googleapis.com/css2?family=Lato:wght@400;700&family=Arimo:wght@400&display=swap">
<style>
  :root {
    --stage: #1f1f1f;
    --card-light: #f1f2f1;
    --card-dark: #1c1d1d;
    --ink: #2a2a2a;
    --accent: #f0491b;
    --white: #ffffff;
  }
  html, body {
    margin: 0;
    padding: 0;
    width: 1200px;
    height: 864px;
    overflow: hidden;
    background: var(--stage);
  }
  .canvas {
    position: relative;
    width: 1200px;
    height: 864px;
  }
  .card {
    position: absolute;
    left: 339px;
    width: 520px;
    height: 305px;
    box-sizing: border-box;
  }
  .card--front {
    top: 95px;
    background: var(--card-light);
  }
  .card--back {
    top: 455px;
    background: var(--card-dark);
  }
  .person {
    position: absolute;
    left: 46px;
    top: 42px;
  }
  .person__name {
    margin: 0;
    font-family: "Lato", sans-serif;
    font-weight: 700;
    font-size: 27px;
    line-height: 32px;
    color: var(--ink);
  }
  .person__role {
    margin: 0;
    font-family: "Lato", sans-serif;
    font-weight: 400;
    font-size: 16px;
    line-height: 20px;
    color: var(--accent);
  }
  .contact {
    position: absolute;
    left: 46px;
    top: 160px;
    margin: 0;
    font-family: "Arimo", sans-serif;
    font-size: 14px;
    line-height: 18px;
  }
  .contact dt { color: var(--accent); }
  .contact dd { margin: 0; color: var(--ink); }
  .brand {
    position: absolute;
    display: flex;
    flex-direction: column;
    align-items: center;
  }
  .brand__dot { display: block; }
  .brand__name {
    font-family: "Lato", sans-serif;
    font-weight: 400;
    letter-spacing: 0.5px;
    white-space: nowrap;
  }
  .card--front .brand {
    left: 272px;
    width: 240px;
    top: 80px;
  }
  .card--front .brand__name {
    margin-top: 22px;
    font-size: 19px;
    color: var(--ink);
  }
  .card--back .brand {
    left: 0;
    width: 520px;
    top: 86px;
  }
  .card--back .brand__name {
    margin-top: 36px;
    font-size: 26px;
    color: var(--white);
  }
</style>
</head>
<body>
<main class="canvas">
  <section class="card card--front" aria-label="Business card front">
    <div class="person">
      <h1 class="person__name">Avery Colton</h1>
      <p class="person__role">Managing Director</p>
    </div>
    <dl class="contact">
      <dt>telephone</dt>
      <dd>044-555 018 273</dd>
      <dt>email</dt>
      <dd>info@orbit-lanternway.example</dd>
      <dt>address</dt>
      <dd>1234, address goes here, country</dd>
    </dl>
    <div class="brand">
      <svg class="brand__dot" width="44" height="44" viewBox="0 0 44 44" aria-hidden="true">
        <circle cx="22" cy="22" r="20" fill="var(--accent)"/>
      </svg>
      <span class="brand__name">ORBIT LANTERNWAY</span>
    </div>
  </section>

  <section class="card card--back" aria-label="Business card back">
    <div class="brand">
      <svg class="brand__dot" width="64" height="64" viewBox="0 0 64 64" aria-hidden="true">
        <circle cx="32" cy="32" r="30" fill="var(--white)"/>
      </svg>
      <span class="brand__name">ORBIT LANTERNWAY</span>
    </div>
  </section>
</main>
</body>
</html>
```